Finance Product Agency Business Card Design

We're an agency that provides products (service contracts, gap insurance, tire and wheel, etc) and support to dealership finance departments. We specialize in training finance producers to maximize their potential and also keep them up to date on the ever changing compliance and legal landscape. I'll attach an image of our logo, excited to see what you all come up with. Would also be interested in discussing our new website design with the winner.

Target Market(s)

auto dealerships

Industry/Entity Type

Business

Contact Information for Business Card

Mark Dolvery
Phone 317.624.5583
Fax 855.472.3308
email Mark.Dolvery@brightlanecoverage.example

Requirements
Must have
• basic contact information
Nice to have
• looking for something professional but modern

```html
<!DOCTYPE html>
<html lang="en">
<head>
<meta charset="utf-8">
<title>Brightlane Coverage Business Card</title>
<link href="https://fonts.googleapis.com/css2?family=Open+Sans:wght@400;600;700&display=swap" rel="stylesheet">
<style>
  :root {
    --backdrop: #3a3a3a;
    --card: #050505;
    --steel: #4f7386;
    --steel-soft: #3e5c6c;
    --white: #f2f2f2;
    --rule: #cfcfcf;
    --ghost: #0e0e0e;
  }
  * { margin: 0; padding: 0; box-sizing: border-box; }
  html, body {
    width: 1200px; height: 900px; overflow: hidden;
    background: var(--backdrop);
    font-family: "Open Sans", Arial, sans-serif;
  }
  .canvas { position: relative; width: 1200px; height: 900px; }
  .card {
    position: absolute; left: 320px; width: 560px; height: 320px;
    background: var(--card); border-radius: 18px; overflow: hidden;
    box-shadow: 0 14px 30px rgba(0,0,0,.55);
  }
  .card--front { top: 90px; }
  .card--contact { top: 470px; }

  .ghost-mark {
    position: absolute; border-radius: 50%; background: var(--ghost);
  }
  .card--front .ghost-mark { left: -70px; top: 150px; width: 220px; height: 220px; }
  .card--contact .ghost-mark { right: -80px; top: -30px; width: 230px; height: 230px; }

  .brand {
    display: flex; align-items: center; gap: 14px;
    color: var(--steel); font-weight: 700; letter-spacing: .04em;
  }
  .brand__dot { border-radius: 50%; background: var(--steel); flex: none; }

  .card--front .brand {
    position: absolute; left: 0; right: 0; top: 100px; justify-content: center;
    font-size: 34px;
  }
  .card--front .brand__dot { width: 40px; height: 40px; }
  .website {
    position: absolute; right: 60px; top: 252px;
    color: var(--white); font-size: 14px;
  }
  .website b { font-weight: 700; }

  .card--contact .brand {
    position: absolute; left: 90px; top: 90px; font-size: 26px;
  }
  .card--contact .brand__dot { width: 32px; height: 32px; }
  .rule-top {
    position: absolute; left: 320px; right: 0; top: 150px; height: 1px; background: var(--rule);
  }
  .contact {
    position: absolute; right: 40px; top: 182px; text-align: right;
    color: var(--white); font-size: 13.5px; line-height: 1.45;
  }
  .contact__name {
    display: flex; align-items: center; justify-content: flex-end; gap: 10px;
    color: var(--steel); font-size: 19px; font-weight: 700; letter-spacing: .03em;
    margin-bottom: 4px;
  }
  .contact__name::before, .contact__name::after {
    content: ""; height: 1px; background: var(--rule);
  }
  .contact__name::before { width: 60px; }
  .contact__name::after { width: 28px; }
  .label { color: var(--steel); font-weight: 600; }
  .rule-bottom {
    position: absolute; left: 0; right: 0; top: 292px; height: 1px; background: var(--rule);
  }
</style>
</head>
<body>
<main class="canvas">
  <section class="card card--front">
    <div class="ghost-mark"></div>
    <div class="brand"><span class="brand__dot"></span>BRIGHTLANE COVERAGE</div>
    <p class="website"><b>www.</b>brightlanecoverage.example</p>
  </section>

  <section class="card card--contact">
    <div class="ghost-mark"></div>
    <div class="brand"><span class="brand__dot"></span>BRIGHTLANE COVERAGE</div>
    <div class="rule-top"></div>
    <div class="contact">
      <p class="contact__name">Mark Dolvery</p>
      <p><span class="label">P:</span> 317.624.5583 &nbsp;<span class="label">F:</span> 855.472.3308</p>
      <p><span class="label">E:</span> Mark.Dolvery@brightlanecoverage.example</p>
    </div>
    <div class="rule-bottom"></div>
  </section>
</main>
</body>
</html>
```